Book Cover for Notes on the Quiet River's Far Lamps

I need a book cover for a 6 x 9 paperback titled Notes on the Quiet River's Far Lamps Gathered by Sailors and Weavers Resting in the Valley beyond the Northern Valley. It has to do with consciousness, the mind, incarnation onto Earth, leaving Earth, and the life in the life after this life. I have an idea I'm providing with this description, but I am open to anything that would be striking and stimulating, whether with a book or not. I am the author, T. Warren Blakely. I've added another background idea to see if anyone can do something with it and I've increased the budget.

```html
<!DOCTYPE html>
<html lang="en">
<head>
<meta charset="utf-8">
<title>Notes on the Quiet River's Far Lamps — Book Cover</title>
<link href="https://fonts.googleapis.com/css2?family=Cinzel:wght@400;600;700&display=swap" rel="stylesheet">
<style>
  :root {
    --backdrop: #e2d4c6;
    --cover-paper: #eeebe6;
    --ink: #1d1b19;
    --sky: #dcd8d1;
    --sand: #9a8c7c;
    --earth: #4a4038;
    --night: #050505;
    --pale-text: #e4ded6;
    --white: #ffffff;
  }
  * { margin: 0; padding: 0; box-sizing: border-box; }
  html, body {
    width: 1200px;
    height: 1200px;
    overflow: hidden;
    background: var(--backdrop);
  }
  .stage {
    width: 1200px;
    height: 1200px;
    display: flex;
    align-items: center;
    justify-content: center;
  }
  .book-cover {
    position: relative;
    width: 720px;
    height: 1080px;
    background: var(--cover-paper);
    overflow: hidden;
    box-shadow: 0 18px 40px rgba(60, 40, 25, 0.25);
    font-family: 'Cinzel', serif;
    color: var(--ink);
  }
  .cover-art {
    position: absolute;
    left: 0;
    top: 340px;
    width: 100%;
    height: 640px;
    background:
      linear-gradient(to bottom,
        rgba(238,235,230,1) 0%,
        rgba(220,216,209,0.9) 12%,
        rgba(205,196,184,0.9) 30%,
        var(--sand) 58%,
        var(--earth) 74%,
        #1c1815 88%,
        var(--night) 100%);
  }
  .cover-art::after {
    content: "";
    position: absolute;
    left: 18%;
    top: 12%;
    width: 64%;
    height: 60%;
    background: radial-gradient(ellipse at center, rgba(230,215,190,0.55) 0%, rgba(230,215,190,0) 70%);
  }
  .title-block {
    position: absolute;
    top: 96px;
    left: 0;
    width: 100%;
    text-align: center;
  }
  .title-main {
    font-size: 104px;
    font-weight: 400;
    letter-spacing: 2px;
    line-height: 1;
  }
  .title-rest {
    margin-top: 28px;
    font-size: 44px;
    font-weight: 400;
    line-height: 1.22;
    letter-spacing: 1px;
  }
  .subtitle {
    position: absolute;
    top: 868px;
    left: 0;
    width: 100%;
    text-align: center;
    font-size: 21px;
    line-height: 1.35;
    color: var(--pale-text);
    letter-spacing: 0.5px;
  }
  .author-band {
    position: absolute;
    left: 0;
    bottom: 0;
    width: 100%;
    height: 124px;
    background: var(--night);
    display: flex;
    align-items: center;
    justify-content: center;
  }
  .author-name {
    font-size: 36px;
    font-weight: 700;
    color: var(--white);
    letter-spacing: 1px;
  }
</style>
</head>
<body>
  <main class="stage">
    <section class="book-cover">
      <div class="cover-art" role="img" aria-label="Surreal photograph of a small woman in a hat pulling open the pages of a giant open book standing on rocky ground beneath a hazy sky"></div>

      <header class="title-block">
        <h1 class="title-main">Notes</h1>
        <p class="title-rest">On the Quiet River's<br>Far Lamps</p>
      </header>

      <p class="subtitle">Gathered by Sailors and Weavers<br>Resting in the Valley<br>beyond the Northern Valley</p>

      <footer class="author-band">
        <p class="author-name">T. Warren Blakely</p>
      </footer>
    </section>
  </main>
</body>
</html>
```